BOLD & MINIMALIST DESIGN NEEDED

We want a very bold but minimalistic business card design that is impactful and utilizes both sides of the business card. Our current logo is included for your use.

We want bold fonts and good use of negative space. We don't want the logo to overpower the design.

Target Market(s)

Professionals who are building new commercial buildings.

Industry/Entity Type

Construction

Contact Information for Business Card

Name, Title, email, office phone, cell phone, website

Font styles to use
Serif
Sans Serif

Requirements
Must have
• Bold design!

```html
<!DOCTYPE html>
<html lang="en">
<head>
<meta charset="utf-8">
<title>Ridgeline Design + Build — Business Card</title>
<link href="https://fonts.googleapis.com/css2?family=Open+Sans:wdth,wght@75..100,300..800&display=swap" rel="stylesheet">
<style>
  :root {
    --backdrop: #a9a9a9;
    --paper: #f7f7f6;
    --charcoal: #2b2b2b;
    --ink: #1f1f1f;
    --lime: #8cc63f;
    --white: #ffffff;
  }
  * { box-sizing: border-box; margin: 0; padding: 0; }
  html, body {
    width: 1200px; height: 1019px; overflow: hidden;
    background: var(--backdrop);
    font-family: "Open Sans", Arial, sans-serif;
  }
  .sheet {
    width: 1200px; height: 1019px;
    display: flex; flex-direction: column; align-items: center; justify-content: center;
    gap: 44px;
  }
  .card {
    position: relative;
    width: 760px; height: 434px;
    border-radius: 34px;
    overflow: hidden;
  }

  /* Front side */
  .card--front { background: var(--paper); color: var(--ink); }
  .front__tab {
    position: absolute; left: 0; top: 38px;
    width: 36px; height: 52px;
    background: var(--lime);
  }
  .front__name {
    position: absolute; left: 52px; top: 34px;
    font-size: 34px; font-weight: 800; font-stretch: 75%;
    letter-spacing: 0.5px; text-transform: uppercase; line-height: 1;
  }
  .front__title {
    position: absolute; left: 52px; top: 74px;
    font-size: 22px; font-weight: 400; line-height: 1;
  }
  .front__brand {
    position: absolute; right: 70px; top: 170px;
    display: flex; align-items: center; gap: 10px;
    font-size: 26px; font-weight: 800; font-stretch: 75%;
    text-transform: uppercase; color: var(--ink);
  }
  .brand__square { width: 16px; height: 16px; background: var(--lime); }
  .front__contacts {
    position: absolute; right: 48px; bottom: 44px;
    list-style: none; text-align: right;
  }
  .contact {
    display: flex; align-items: center; justify-content: flex-end; gap: 12px;
    font-size: 19px; font-weight: 600; font-stretch: 87%;
    line-height: 30px;
  }
  .contact svg { width: 18px; height: 18px; fill: var(--lime); flex: none; }

  /* Back side */
  .card--back { background: var(--charcoal); color: var(--white); }
  .back__brand {
    position: absolute; left: 0; right: 0; top: 176px;
    display: flex; align-items: center; justify-content: center; gap: 14px;
    font-size: 44px; font-weight: 800; font-stretch: 75%;
    text-transform: uppercase; letter-spacing: 1px; color: var(--white);
  }
  .back__brand .brand__square { width: 24px; height: 24px; }
  .back__band {
    position: absolute; left: 0; right: 0; top: 268px; height: 64px;
    background: var(--lime);
    display: flex; align-items: center; justify-content: center;
  }
  .back__web {
    font-size: 24px; font-weight: 500; font-stretch: 87%;
    letter-spacing: 4px; color: var(--charcoal);
  }
</style>
</head>
<body>
<main class="sheet">
  <section class="card card--front" aria-label="Business card front">
    <div class="front__tab"></div>
    <h1 class="front__name">Daniel Marsh</h1>
    <p class="front__title">Manager</p>
    <div class="front__brand"><span>Ridgeline</span><span class="brand__square"></span></div>
    <ul class="front__contacts">
      <li class="contact">021-555-0148
        <svg viewBox="0 0 24 24" aria-hidden="true"><path d="M6.6 10.8a15.1 15.1 0 0 0 6.6 6.6l2.2-2.2a1 1 0 0 1 1-.25 11.4 11.4 0 0 0 3.6.57 1 1 0 0 1 1 1V20a1 1 0 0 1-1 1A17 17 0 0 1 3 4a1 1 0 0 1 1-1h3.5a1 1 0 0 1 1 1c0 1.25.2 2.45.57 3.57a1 1 0 0 1-.25 1z"/></svg>
      </li>
      <li class="contact">+5642 555 0192
        <svg viewBox="0 0 24 24" aria-hidden="true"><path d="M7 2h10a2 2 0 0 1 2 2v16a2 2 0 0 1-2 2H7a2 2 0 0 1-2-2V4a2 2 0 0 1 2-2zm0 3v13h10V5zm5 14.2a1 1 0 1 0 0 .01z"/></svg>
      </li>
      <li class="contact">daniel@ridgelinebuild.com
        <svg viewBox="0 0 24 24" aria-hidden="true"><path d="M3 5h18a1 1 0 0 1 1 1v12a1 1 0 0 1-1 1H3a1 1 0 0 1-1-1V6a1 1 0 0 1 1-1zm1 2.2V17h16V7.2l-8 5.3z M4.6 7 12 11.9 19.4 7z"/></svg>
      </li>
    </ul>
  </section>

  <section class="card card--back" aria-label="Business card back">
    <div class="back__brand"><span>Ridgeline</span><span class="brand__square"></span></div>
    <div class="back__band"><p class="back__web">www.ridgelinebuild.com</p></div>
  </section>
</main>
</body>
</html>
```